Hadley & Partners, LLC Business Card 2016

We need a new business card design for a very important trade show coming up.

We are a compliance Consulting Firm. Our clients are stock brokerage firms and investment advisers.

I would like our logo on both sides of the card.

Info in the front of the card shold include:

Logo
First & Last Name
Title
Office #
Cell #
Email
Company Address (42 W. Calloway St., Suite 300 Pasadena, CA 91417

Back of the card should include the logo and url: www.hadleypartnersgroup.com

Target Market(s)

Stock Brokerage Firms and Investment Advisers

Industry/Entity Type

Financial Service

Contact Information for Business Card

Marcus J. Pellew
President
42 W. Calloway St., Suite 300
Pasadena, CA 91417
O 626.555.0147 ext. 204
C 818.555.0193
Email: marcus@hadleypartnersgroup.com
www.hadleypartnersgroup.com

Requirements
Nice to have
• The back of the card could be black with the logo with the white letters.
• I do want the front of the card to at least have the color logo with the black "Hadley & Partners Lettering.

```html
<!DOCTYPE html>
<html lang="en">
<head>
<meta charset="utf-8">
<title>Hadley &amp; Partners — Business Card</title>
<link href="https://fonts.googleapis.com/css2?family=Lato:wght@400;700;900&display=swap" rel="stylesheet">
<style>
  :root {
    --stage: #1d1e21;
    --ink: #1b1b1e;
    --panel: #2a2b30;
    --charcoal: #3b3c42;
    --red: #e0202e;
    --red-deep: #b3141f;
    --white: #ffffff;
    --soft: #d9d9dc;
  }
  * { box-sizing: border-box; margin: 0; padding: 0; }
  html, body { width: 1200px; height: 1000px; overflow: hidden; }
  body {
    background: var(--stage);
    font-family: "Lato", Arial, sans-serif;
    position: relative;
  }
  .card {
    position: absolute;
    width: 630px;
    height: 360px;
    border-radius: 22px;
    overflow: hidden;
  }
  .card-shapes { position: absolute; inset: 0; width: 100%; height: 100%; }
  .card--front { left: 285px; top: 90px; background: var(--white); }
  .card--back { left: 285px; top: 550px; background: var(--panel); }

  .holder { position: absolute; left: 34px; top: 24px; }
  .holder-name {
    font-size: 18px; font-weight: 900; letter-spacing: 1.5px;
    color: var(--soft); text-transform: uppercase;
  }
  .holder-name .surname { color: var(--red); }
  .holder-title { font-size: 16px; font-weight: 700; color: var(--white); margin-top: 2px; }
  .holder-rule { width: 86px; height: 2px; background: var(--red); margin-top: 6px; }

  .contact-row {
    position: absolute; left: 24px;
    display: flex; align-items: center; gap: 12px;
    color: var(--white); font-size: 13.5px; line-height: 1.3;
  }
  .contact-row--phone { top: 96px; }
  .contact-row--email { top: 163px; }
  .contact-row--address { top: 223px; }
  .contact-icon { width: 30px; height: 30px; flex: none; }

  .brand {
    position: absolute; display: flex; align-items: center; gap: 10px;
  }
  .brand-square { width: 26px; height: 26px; background: var(--red); flex: none; }
  .brand-name {
    font-weight: 700; font-size: 19px; letter-spacing: 2px; line-height: 1.15;
    text-transform: uppercase; white-space: nowrap;
  }
  .card--front .brand { left: 442px; top: 152px; }
  .card--front .brand-name { color: var(--ink); }
  .card--back .brand { left: 205px; top: 120px; }
  .card--back .brand-square { width: 40px; height: 40px; }
  .card--back .brand-name { color: var(--white); font-size: 28px; }

  .web-url {
    position: absolute; left: 30px; top: 326px;
    display: flex; align-items: center; gap: 8px;
    color: var(--white); font-size: 15px;
  }
  .web-url svg { width: 18px; height: 18px; }
</style>
</head>
<body>

<section class="card card--front" aria-label="Business card front">
  <svg class="card-shapes" viewBox="0 0 630 360" aria-hidden="true">
    <polygon points="0,0 345,0 345,300 0,300" fill="var(--panel)"/>
    <polygon points="0,90 362,90 384,117 362,144 0,144" fill="var(--red)"/>
    <polygon points="0,152 394,152 416,178 394,204 0,204" fill="var(--charcoal)"/>
    <polygon points="0,212 358,212 380,238 358,264 0,264" fill="var(--red)"/>
    <polygon points="0,288 250,288 274,318 0,318" fill="var(--red-deep)"/>
    <rect x="0" y="318" width="630" height="42" fill="var(--red)"/>
  </svg>

  <div class="holder">
    <p class="holder-name">Marcus J. <span class="surname">Pellew</span></p>
    <p class="holder-title">President</p>
    <div class="holder-rule"></div>
  </div>

  <div class="contact-row contact-row--phone">
    <svg class="contact-icon" viewBox="0 0 30 30" aria-hidden="true">
      <circle cx="15" cy="15" r="15" fill="var(--panel)"/>
      <path d="M10.5 8.5l3 0 1 4-2 1.2a8 8 0 0 0 3.8 3.8l1.2-2 4 1v3a1.5 1.5 0 0 1-1.6 1.5A12 12 0 0 1 9 10.1 1.5 1.5 0 0 1 10.5 8.5z" fill="var(--white)"/>
    </svg>
    <p>818.555.0193<br>626.555.0147 (ext. 204)</p>
  </div>

  <div class="contact-row contact-row--email">
    <svg class="contact-icon" viewBox="0 0 30 30" aria-hidden="true">
      <circle cx="15" cy="15" r="15" fill="var(--panel)"/>
      <g fill="none" stroke="var(--white)" stroke-width="1.3">
        <circle cx="15" cy="15" r="7"/>
        <ellipse cx="15" cy="15" rx="3" ry="7"/>
        <line x1="8" y1="15" x2="22" y2="15"/>
      </g>
    </svg>
    <p>marcus@hadleypartnersgroup.com</p>
  </div>

  <div class="contact-row contact-row--address">
    <svg class="contact-icon" viewBox="0 0 30 30" aria-hidden="true">
      <circle cx="15" cy="15" r="15" fill="var(--panel)"/>
      <path d="M15 7a5.5 5.5 0 0 0-5.5 5.5c0 4 5.5 10.5 5.5 10.5s5.5-6.5 5.5-10.5A5.5 5.5 0 0 0 15 7z" fill="var(--white)"/>
      <circle cx="15" cy="12.5" r="2" fill="var(--panel)"/>
    </svg>
    <p>42 W. Calloway St., Suite 300<br>Pasadena, CA 91417</p>
  </div>

  <div class="brand">
    <span class="brand-square"></span>
    <p class="brand-name">Hadley &amp;<br>Partners</p>
  </div>
</section>

<section class="card card--back" aria-label="Business card back">
  <svg class="card-shapes" viewBox="0 0 630 360" aria-hidden="true">
    <polygon points="0,292 200,292 222,314 630,314 630,360 0,360" fill="var(--red)"/>
    <polygon points="0,0 26,0 26,292 0,292" fill="var(--red)"/>
    <polygon points="604,0 630,0 630,314 604,314 604,0" fill="var(--red-deep)"/>
  </svg>

  <div class="brand">
    <span class="brand-square"></span>
    <p class="brand-name">Hadley &amp;<br>Partners</p>
  </div>

  <p class="web-url">
    <svg viewBox="0 0 18 18" aria-hidden="true">
      <g fill="none" stroke="var(--white)" stroke-width="1.2">
        <circle cx="9" cy="9" r="7.5"/>
        <ellipse cx="9" cy="9" rx="3.2" ry="7.5"/>
        <line x1="1.5" y1="9" x2="16.5" y2="9"/>
      </g>
    </svg>
    hadleypartnersgroup.com
  </p>
</section>

</body>
</html>
```